Branding label contest for 2 great products

I require labels for our health food treat dry packs and coffee business. The packaging at this stage consists of the follow... plastic food pouches for dry ingredients and takeaway coffee cups. The coffee cup artwork/design will be for standard small, medium and large paper takeaway coffee cups and the food pouch size 190mmW x 260mmL. the pouch design will need to be customisable to allow use across a range of products. for reference please visit www.torvimelu.com.au and instagram @torvimelu for products. I have attached our logo and business card files for your perusal.

Target Market(s)

Healthy conscious, vegan, paleo, gluten free, all round fitness fanatics and yogis

Industry/Entity Type

Business

Requirements
Must have
• Earthy tones, our logo. Rustic earthy feel. trendy artwork.
Should not have
• Bright colours

```html
<!DOCTYPE html>
<html lang="en">
<head>
<meta charset="utf-8">
<title>Torvi Melu — Pouch and Cup Labels</title>
<link rel="stylesheet" href="https://fonts.googleapis.com/css2?family=Dancing+Script:wght@700&family=Montserrat:wght@400;600&display=swap">
<style>
  :root {
    --bg: #e4e4e4;
    --pouch: #ffffff;
    --pouch-shade: #ececec;
    --ink-light: #ffffff;

    --maroon: #5c292c;
    --maroon-band: #a87473;
    --maroon-badge: #f1e9e2;
    --maroon-mark: #9b5b5d;

    --forest: #3e5835;
    --forest-band: #a3bb98;
    --forest-badge: #a8c59c;
    --forest-mark: #ffffff;

    --cocoa: #6a4533;
    --cocoa-band: #b6a98e;
    --cocoa-badge: #c8b89f;
    --cocoa-mark: #ffffff;

    --script: "Dancing Script", cursive;
    --sans: "Montserrat", sans-serif;
  }
  * { box-sizing: border-box; margin: 0; padding: 0; }
  html, body { width: 1200px; height: 1051px; overflow: hidden; }
  body { background: var(--bg); position: relative; font-family: var(--sans); }

  /* ---------- Pouch ---------- */
  .pouch {
    position: absolute;
    width: 400px; height: 542px;
    background: linear-gradient(180deg, var(--pouch) 0%, var(--pouch) 92%, var(--pouch-shade) 100%);
    box-shadow: 0 4px 14px rgba(0,0,0,.18);
    transform-origin: top left;
  }
  .pouch--large { left: 138px; top: 46px; }
  .pouch--small { transform: scale(.46); top: 680px; }
  .pouch--forest { left: 142px; }
  .pouch--cocoa { left: 354px; }

  .pouch__seal {
    position: absolute; left: 0; right: 0; top: 4px; height: 14px;
    background: repeating-linear-gradient(180deg, #dcdcdc 0 1px, transparent 1px 4px);
  }
  .pouch__band {
    position: absolute; left: 0; right: 0; top: 154px; height: 244px;
    background: var(--band);
  }
  .pouch__disc {
    position: absolute; left: 28px; top: 112px;
    width: 340px; height: 340px; border-radius: 50%;
    background: var(--tone);
    display: flex; flex-direction: column; align-items: center;
    color: var(--ink-light);
  }
  .pouch__name {
    font-family: var(--script);
    font-size: 56px; line-height: .92;
    margin-top: 88px; text-align: center;
  }
  .pouch__name span { display: block; }
  .pouch__name span + span { font-size: 66px; padding-left: 60px; }
  .rule { width: 28px; height: 1.5px; background: currentColor; opacity: .9; }
  .pouch__disc .rule:first-of-type { margin-top: 34px; }
  .pouch__tagline {
    font-size: 9.5px; font-weight: 600; letter-spacing: 1.6px;
    text-align: center; line-height: 1.25; margin: 10px 0;
  }
  .pouch__weight {
    position: absolute; left: 0; right: 0; top: 476px;
    text-align: center; font-size: 20px; color: var(--band);
  }

  .badge {
    position: absolute; border-radius: 50%;
    background: var(--badge);
    display: flex; align-items: center; justify-content: center;
    font-family: var(--sans); font-weight: 600;
    color: var(--mark); text-align: center; line-height: 1.2;
  }
  .pouch .badge {
    left: 146px; top: 54px; width: 106px; height: 106px;
    font-size: 12px; letter-spacing: 2px; z-index: 2;
  }

  .theme--maroon { --tone: var(--maroon); --band: var(--maroon-band); --badge: var(--maroon-badge); --mark: var(--maroon-mark); }
  .theme--forest { --tone: var(--forest); --band: var(--forest-band); --badge: var(--forest-badge); --mark: var(--forest-mark); }
  .theme--cocoa  { --tone: var(--cocoa);  --band: var(--cocoa-band);  --badge: var(--cocoa-badge);  --mark: var(--cocoa-mark); }

  /* ---------- Cup wrap ---------- */
  .cup {
    position: absolute;
    background: var(--tone);
    clip-path: polygon(0 0, 100% 0, 91% 100%, 9% 100%);
    color: var(--ink-light);
    display: flex; flex-direction: column; align-items: center;
  }
  .cup--forest { left: 670px; top: 330px; width: 240px; height: 380px; }
  .cup--maroon {
    left: 850px; top: 300px; width: 320px; height: 470px;
    filter: drop-shadow(0 6px 10px rgba(0,0,0,.2));
  }
  .cup .badge { position: static; }
  .cup--maroon .badge { width: 92px; height: 92px; margin-top: 54px; font-size: 10.5px; letter-spacing: 1.8px; }
  .cup--forest .badge { width: 70px; height: 70px; margin-top: 44px; font-size: 8px; letter-spacing: 1.4px; }
  .cup__name { font-family: var(--script); line-height: 1; }
  .cup--maroon .cup__name { font-size: 70px; margin-top: 44px; }
  .cup--forest .cup__name { font-size: 52px; margin-top: 34px; }
  .cup .rule { width: 22px; }
  .cup--maroon .rule:first-of-type { margin-top: 44px; }
  .cup--forest .rule:first-of-type { margin-top: 34px; }
  .cup__tagline { font-weight: 600; letter-spacing: 1.6px; text-align: center; line-height: 1.25; margin: 8px 0; }
  .cup--maroon .cup__tagline { font-size: 9px; }
  .cup--forest .cup__tagline { font-size: 7px; }
</style>
</head>
<body>

  <article class="pouch pouch--large theme--maroon">
    <div class="pouch__seal"></div>
    <div class="pouch__band"></div>
    <div class="badge">TORVI<br>MELU</div>
    <div class="pouch__disc">
      <h2 class="pouch__name"><span>Product</span><span>Name</span></h2>
      <div class="rule"></div>
      <p class="pouch__tagline">LOREM IPSUM DOLOR<br>SIT AMET</p>
      <div class="rule"></div>
    </div>
    <p class="pouch__weight">50g</p>
  </article>

  <article class="pouch pouch--small pouch--forest theme--forest">
    <div class="pouch__seal"></div>
    <div class="pouch__band"></div>
    <div class="badge">TORVI<br>MELU</div>
    <div class="pouch__disc">
      <h2 class="pouch__name"><span>Product</span><span>Name</span></h2>
      <div class="rule"></div>
      <p class="pouch__tagline">LOREM IPSUM DOLOR<br>SIT AMET</p>
      <div class="rule"></div>
    </div>
    <p class="pouch__weight">50g</p>
  </article>

  <article class="pouch pouch--small pouch--cocoa theme--cocoa">
    <div class="pouch__seal"></div>
    <div class="pouch__band"></div>
    <div class="badge">TORVI<br>MELU</div>
    <div class="pouch__disc">
      <h2 class="pouch__name"><span>Product</span><span>Name</span></h2>
      <div class="rule"></div>
      <p class="pouch__tagline">LOREM IPSUM DOLOR<br>SIT AMET</p>
      <div class="rule"></div>
    </div>
    <p class="pouch__weight">50g</p>
  </article>

  <article class="cup cup--forest theme--forest">
    <div class="badge">TORVI<br>MELU</div>
    <h2 class="cup__name">Coffee</h2>
    <div class="rule"></div>
    <p class="cup__tagline">LOREM IPSUM DOLOR<br>SIT AMET</p>
    <div class="rule"></div>
  </article>

  <article class="cup cup--maroon theme--maroon">
    <div class="badge">TORVI<br>MELU</div>
    <h2 class="cup__name">Coffee</h2>
    <div class="rule"></div>
    <p class="cup__tagline">LOREM IPSUM DOLOR<br>SIT AMET</p>
    <div class="rule"></div>
  </article>

</body>
</html>
```